New Stationery and envelope Design Project

I need business envelopes and stationary. I would like to have office locations on both (only Chicago address) which are Chicago (Elm Crest), Washington, Mexico City, Bogota. Of course in formats I can upload and have printed. Simple and very professional I am looking for. The return address/stationary address should be:

2867 North Pellam Avenue
Annex Level
Elm Crest, Ohio 60871

Target Market(s)

I am a consultant for larger corporations

Industry/Entity Type

Consulting

Colors

Designer to choose colors to be used in the design.

Requirements
Must have
• our address, logo, very professional and clean.
Nice to have
• the names of the cities we have offices.

```html
<!DOCTYPE html>
<html lang="en">
<head>
<meta charset="utf-8">
<title>Lakeline Advisory — Stationery Set</title>
<link rel="stylesheet" href="https://fonts.googleapis.com/css2?family=Lato:wght@400;700&display=swap">
<style>
  :root {
    --canvas: #e9e9e9;
    --paper: #f7f7f8;
    --navy: #1b4670;
    --navy-deep: #163d63;
    --brand-blue: #24409a;
    --accent-blue: #2f7fd0;
    --text-grey: #6d6f73;
    --text-dark: #4a4c50;
    --window-grey: #eaeaec;
  }
  * { box-sizing: border-box; margin: 0; padding: 0; }
  html, body { width: 1200px; height: 1200px; overflow: hidden; }
  body {
    background: var(--canvas);
    font-family: "Lato", sans-serif;
    position: relative;
  }
  .sheet, .envelope, .card { position: absolute; background: var(--paper); overflow: hidden; }

  /* Letterhead */
  .letterhead { left: 130px; top: 274px; width: 442px; height: 626px; }
  .brand-mark {
    position: absolute; border-radius: 50%; background: var(--accent-blue);
  }
  .brand-name {
    position: absolute; white-space: nowrap; font-weight: 400;
    color: var(--brand-blue); letter-spacing: 0.02em; transform: translateX(-50%);
  }
  .letterhead .brand-mark { left: 336px; top: 42px; width: 28px; height: 28px; }
  .letterhead .brand-name { left: 350px; top: 100px; font-size: 13px; }
  .salutation {
    position: absolute; left: 48px; top: 197px; font-size: 7px; color: var(--brand-blue);
  }
  .letter-body {
    position: absolute; left: 48px; top: 224px; width: 340px;
    font-size: 6.6px; line-height: 9px; color: var(--text-grey);
  }
  .letter-body p { margin-bottom: 17px; }
  .closing {
    position: absolute; left: 48px; top: 425px;
    font-size: 6.8px; line-height: 9px; color: var(--text-grey);
  }
  .closing strong { color: var(--text-dark); }
  .signature {
    position: absolute; left: 52px; top: 466px; width: 78px; height: 60px;
    background: linear-gradient(135deg, #dfe4f1, #eef0f6); border-radius: 4px;
  }
  .letter-footer {
    position: absolute; left: 26px; top: 596px; display: flex; gap: 12px;
    font-size: 6.6px; color: var(--text-dark); white-space: nowrap;
  }
  .letter-footer span { display: flex; align-items: center; gap: 4px; }
  .icon { width: 6px; height: 6px; flex: none; }

  /* Envelope back */
  .envelope-back { left: 611px; top: 276px; width: 495px; height: 236px; }
  .flap { position: absolute; left: 0; top: 0; width: 495px; height: 82px; }
  .flap-name {
    position: absolute; left: 50%; top: 35px; transform: translateX(-50%);
    color: #ffffff; font-size: 12.5px; letter-spacing: 0.02em; white-space: nowrap;
  }

  /* Envelope front */
  .envelope-front { left: 610px; top: 530px; width: 496px; height: 238px; }
  .address-window {
    position: absolute; left: 27px; top: 29px; width: 135px; height: 48px;
    background: var(--window-grey); border: 1px solid #d6d7da; border-radius: 7px;
  }
  .return-address {
    position: absolute; left: 27px; top: 86px; display: flex; gap: 4px;
    font-size: 7.6px; line-height: 9.5px; color: var(--text-dark);
  }
  .envelope-front .brand-mark { left: 415px; top: 38px; width: 22px; height: 22px; }
  .envelope-front .brand-name { left: 426px; top: 79px; font-size: 9px; }

  /* Business cards */
  .card-front { left: 612px; top: 787px; width: 199px; height: 114px; }
  .holder-name {
    position: absolute; left: 14px; top: 26px; font-size: 5.2px; font-weight: 700; color: var(--brand-blue);
  }
  .holder-title {
    position: absolute; left: 14px; top: 33px; font-size: 4.6px; color: var(--text-grey);
  }
  .holder-rule {
    position: absolute; left: 14px; top: 41px; width: 49px; height: 1px; background: #9aa0ab;
  }
  .card-contact {
    position: absolute; left: 14px; top: 64px; font-size: 4.2px; line-height: 5.4px; color: var(--text-grey);
  }
  .card-contact .row { display: flex; gap: 3px; }
  .card-contact .gap { height: 3px; }
  .card-contact .icon { width: 4px; height: 4px; margin-top: 0.5px; }
  .card-front .brand-mark { left: 148px; top: 22px; width: 16px; height: 16px; }
  .card-front .brand-name { left: 156px; top: 51px; font-size: 5.8px; }

  .card-back { left: 834px; top: 787px; width: 200px; height: 114px; background: var(--navy-deep); }
  .card-back .brand-mark { left: 88px; top: 39px; width: 22px; height: 22px; }
  .card-back .brand-name { left: 99px; top: 75px; font-size: 7.4px; color: #ffffff; }
</style>
</head>
<body>

  <!-- Letterhead -->
  <section class="sheet letterhead">
    <span class="brand-mark"></span>
    <span class="brand-name">LAKELINE ADVISORY</span>

    <p class="salutation">Dear Mr. Peter Lane</p>

    <div class="letter-body">
      <p>Lorem ipsum dolor sit amet, consectetuer adipiscing elit. Aenean commodo ligula eget dolor. Aenean massa. Cum sociis natoque penatibus et magnis dis parturient montes, nascetur ridiculus mus. Donec quam felis, ultricies nec, pellentesque eu, pretium quis, sem. Nulla consequat massa quis enim. Donec pede justo, fringilla vel, aliquet nec, vulputate eget, arcu.</p>
      <p>In enim justo, rhoncus ut, imperdiet a, venenatis vitae, justo. Nullam dictum felis eu pede mollis pretium. Integer tincidunt. Cras dapibus. Vivamus elementum semper nisi. Aenean vulputate eleifend tellus. Aenean leo ligula, porttitor eu, consequat vitae, eleifend ac, enim. Aliquam lorem ante, dapibus in, viverra quis, feugiat a, tellus.</p>
      <p>Phasellus viverra nulla ut metus varius laoreet. Quisque rutrum. Aenean imperdiet. Etiam ultricies nisi vel augue. Curabitur ullamcorper ultricies nisi. Nam eget dui. Etiam rhoncus. Maecenas tempus, tellus eget condimentum rhoncus, sem quam semper libero, sit amet adipiscing sem neque sed ipsum. Nam quam nunc, blandit vel, luctus pulvinar, hendrerit id, lorem. Maecenas nec odio et ante tincidunt tempus. Donec vitae sapien ut libero venenatis faucibus. Nullam quis ante. Etiam sit amet orci eget eros faucibus tincidunt. Duis leo. Sed fringilla mauris sit amet nibh. Donec sodales sagittis magna. Sed consequat, leo eget bibendum sodales, augue velit cursus nunc,</p>
    </div>

    <div class="closing">
      <strong>Sincerely,</strong><br>
      Morgan<br>
      General Manager
    </div>

    <div class="signature" role="img" aria-label="Handwritten signature of the general manager"></div>

    <footer class="letter-footer">
      <span>
        <svg class="icon" viewBox="0 0 10 10"><path d="M5 0.5a3.2 3.2 0 0 0-3.2 3.2C1.8 6.2 5 9.5 5 9.5s3.2-3.3 3.2-5.8A3.2 3.2 0 0 0 5 0.5z" fill="var(--brand-blue)"/><circle cx="5" cy="3.7" r="1.2" fill="#fff"/></svg>
        2867 North Pellam Avenue, Annex Level, Elm Crest, Ohio 60871
      </span>
      <span>
        <svg class="icon" viewBox="0 0 10 10"><circle cx="5" cy="5" r="4.2" fill="none" stroke="var(--brand-blue)" stroke-width="1.3"/><path d="M1 5h8M5 1c-2 2.5-2 5.5 0 8M5 1c2 2.5 2 5.5 0 8" fill="none" stroke="var(--brand-blue)" stroke-width="0.9"/></svg>
        www.lakelineadvisory.com
      </span>
      <span>
        <svg class="icon" viewBox="0 0 10 10"><rect x="0.8" y="2" width="8.4" height="6" rx="0.8" fill="var(--brand-blue)"/><path d="M1 2.4L5 5.6 9 2.4" fill="none" stroke="#fff" stroke-width="0.9"/></svg>
        hello@lakelineadvisory.com
      </span>
    </footer>
  </section>

  <!-- Envelope, back with flap -->
  <section class="envelope envelope-back">
    <svg class="flap" viewBox="0 0 495 82" preserveAspectRatio="none">
      <path d="M0 0H495V0L487 72Q486 80 477 81L20 82Q10 82 9 72Z" fill="var(--navy)"/>
    </svg>
    <span class="flap-name">LAKELINE ADVISORY</span>
  </section>

  <!-- Envelope, front -->
  <section class="envelope envelope-front">
    <div class="address-window"></div>
    <div class="return-address">
      <svg class="icon" viewBox="0 0 10 10"><path d="M5 0.5a3.2 3.2 0 0 0-3.2 3.2C1.8 6.2 5 9.5 5 9.5s3.2-3.3 3.2-5.8A3.2 3.2 0 0 0 5 0.5z" fill="var(--brand-blue)"/><circle cx="5" cy="3.7" r="1.2" fill="#fff"/></svg>
      <div>2867 North Pellam Avenue, Annex Level<br>Elm Crest, Ohio 60871</div>
    </div>
    <span class="brand-mark"></span>
    <span class="brand-name">LAKELINE ADVISORY</span>
  </section>

  <!-- Business card, front -->
  <section class="card card-front">
    <p class="holder-name">Daniel Reyes</p>
    <p class="holder-title">Founder and Principal</p>
    <span class="holder-rule"></span>
    <div class="card-contact">
      <div class="row">
        <svg class="icon" viewBox="0 0 10 10"><path d="M5 0.5a3.2 3.2 0 0 0-3.2 3.2C1.8 6.2 5 9.5 5 9.5s3.2-3.3 3.2-5.8A3.2 3.2 0 0 0 5 0.5z" fill="var(--brand-blue)"/></svg>
        <div>2867 North Pellam Avenue<br>Annex Level<br>Elm Crest, Ohio 60871</div>
      </div>
      <div class="gap"></div>
      <div class="row">
        <svg class="icon" viewBox="0 0 10 10"><rect x="0.8" y="2" width="8.4" height="6" rx="0.8" fill="var(--brand-blue)"/></svg>
        <div>daniel@lakelineadvisory.com</div>
      </div>
      <div class="row">
        <svg class="icon" viewBox="0 0 10 10"><circle cx="5" cy="5" r="4.2" fill="var(--brand-blue)"/></svg>
        <div>www.lakelineadvisory.com</div>
      </div>
    </div>
    <span class="brand-mark"></span>
    <span class="brand-name">LAKELINE ADVISORY</span>
  </section>

  <!-- Business card, back -->
  <section class="card card-back">
    <span class="brand-mark"></span>
    <span class="brand-name">LAKELINE ADVISORY</span>
  </section>

</body>
</html>
```